Social Media Graphics - Copperfield Loop

Create 6-7 individual social media graphics (square size) to encourage folks to join our online course, using either of the text below (only one set of text per graphic:

The Lantern Ridge Method
How to Create a 7-Figure Business From Scratch
Sign Up Today!

Or

The Lantern Ridge Method
Fast-track Your Way to a Multi-Million Business!
Sign Up Today!

For the color scheme of the graphics, use 1 or 2 colors in the color palette attached; or use any colors that look nice with their outfits; AVOID using red, white and blue altogether because it will look like an Independence Day (4th of July) graphic and we don’t want that; make sure the graphics appeal to both men and women

Make sure each graphic contains 1 of the 2 pics attached; and make sure one of the graphics is all TEXT only.

Target Market(s)

men and women looking to make more money

Industry/Entity Type

entrepreneurship

Requirements
Must have
• see the text document attached
Nice to have
• We are open to a nice color design; the color palette colors are not required, especially we don't want red, white and blue used together
Should not have
• AVOID using red, white and blue altogether because it will look like an Independence Day (4th of July) graphic and we dont want that

```html
<!DOCTYPE html>
<html lang="en">
<head>
<meta charset="utf-8">
<title>Copperfield Loop – Course Social Graphics</title>
<link href="https://fonts.googleapis.com/css2?family=Montserrat:wght@300;400;600;700;800&display=swap" rel="stylesheet">
<style>
  :root {
    --page-bg: #dedede;
    --navy-deep: #020826;
    --navy-glow: #0c1d45;
    --gold: #d8b462;
    --brand-blue: #0b4a8c;
    --ink-dark: #0a0f24;
    --ink-soft: #2a2a2a;
    --white: #ffffff;
  }
  * { margin: 0; padding: 0; box-sizing: border-box; }
  html, body {
    width: 1200px; height: 1000px; overflow: hidden;
    background: var(--page-bg);
    font-family: "Montserrat", sans-serif;
  }
  .graphic {
    position: absolute; top: 241px;
    width: 518px; height: 518px;
    overflow: hidden;
  }
  .graphic--text-only {
    left: 54px;
    background: radial-gradient(circle at 50% 48%, var(--navy-glow) 0%, var(--navy-deep) 62%);
  }
  .graphic--photo { left: 627px; background: var(--gold); }

  /* Text-only graphic */
  .title-kicker {
    position: absolute; top: 54px; left: 111px; width: 295px; height: 24px;
    display: flex; align-items: center; justify-content: space-between;
  }
  .title-kicker__rule { width: 73px; height: 4px; background: var(--gold); }
  .title-kicker__word {
    color: var(--white); font-weight: 800; font-size: 25px; letter-spacing: 19px;
    margin-right: -19px;
  }
  .title-name {
    position: absolute; top: 92px; left: 100px; width: 318px;
    text-align: center; color: var(--white);
    font-weight: 800; font-size: 35px; letter-spacing: -0.5px; line-height: 60px;
  }
  .title-tag {
    position: absolute; top: 161px; left: 111px; width: 295px; height: 50px;
    background: var(--gold); color: var(--ink-dark);
    font-weight: 700; font-size: 37px; line-height: 50px; text-align: center;
  }
  .headline { position: absolute; left: 0; width: 100%; text-align: center; font-weight: 700; font-size: 31px; line-height: 43px; color: var(--white); }
  .headline--top { top: 258px; }
  .headline--band { top: 301px; height: 43px; background: var(--gold); }
  .headline--bottom { top: 344px; }

  .cta {
    position: absolute; top: 437px; height: 34px; width: 186px;
    border: 2px solid var(--white); border-radius: 17px;
    color: var(--white); font-weight: 700; font-size: 17px;
    display: flex; align-items: center; justify-content: center;
  }
  .graphic--text-only .cta { left: 166px; }
  .graphic--photo .cta { left: 167px; background: var(--brand-blue); z-index: 2; }

  /* Photo graphic */
  .sub-line {
    position: absolute; left: 0; width: 100%; text-align: center;
    color: var(--ink-soft); font-weight: 300; font-size: 21px; letter-spacing: 7px;
  }
  .sub-line--top { top: 30px; }
  .sub-line--bottom { top: 103px; }
  .feature-line {
    position: absolute; top: 58px; left: 0; width: 100%; text-align: center;
    color: var(--brand-blue); font-weight: 800; font-size: 37px; letter-spacing: -0.5px;
  }
  .hosts-photo {
    position: absolute; left: 47px; top: 143px; width: 420px; height: 375px;
    border-radius: 120px 120px 0 0;
    background: linear-gradient(100deg, #1f1f24 0%, #2b2b30 48%, #1b4f86 60%, #20242e 100%);
  }
</style>
</head>
<body>

<section class="graphic graphic--text-only">
  <div class="title-kicker">
    <span class="title-kicker__rule"></span>
    <span class="title-kicker__word">THE</span>
    <span class="title-kicker__rule"></span>
  </div>
  <div class="title-name">LANTERN RIDGE</div>
  <div class="title-tag">METHOD</div>

  <div class="headline headline--top">HOW TO CREATE</div>
  <div class="headline headline--band">A 7-FIGURE BUSINESS</div>
  <div class="headline headline--bottom">FROM SCRATCH</div>

  <div class="cta">SIGN UP TODAY!</div>
</section>

<section class="graphic graphic--photo">
  <div class="sub-line sub-line--top">HOW TO CREATE</div>
  <div class="feature-line">A 7-FIGURE BUSINESS</div>
  <div class="sub-line sub-line--bottom">FROM SCRATCH</div>

  <div class="hosts-photo" role="img" aria-label="Photo of the two course hosts standing together, a man in a black turtleneck with arms crossed and a woman in a blue denim jacket"></div>

  <div class="cta">SIGN UP TODAY!</div>
</section>

</body>
</html>
```